Hedge fund needs power point design for marketing pitch

We need a designer to make our power point pitch more aesthetically appealing to potential clients. We will be marketing our hedge fund to high net worth individuals and financial institutions. The ideal design will look professional and project confidence to our potential clients. We have attached a rough outline of what we have completed so far. We have also attached example cover pages for 2 pitch books produced by our competitors.

Target Market(s)

Financial institutions and wealthy investors

Industry/Entity Type

Finance

Requirements
Must have
• must use our logo and current slides. Must look professional

```html
<!DOCTYPE html>
<html lang="en">
<head>
<meta charset="utf-8">
<title>Why Invest? – Calloway Derivatives Fund, LP</title>
<link href="https://fonts.googleapis.com/css2?family=Tinos:wght@400;700&display=swap" rel="stylesheet">
<style>
  :root {
    --panel-green: #1d4a2e;
    --field-green: #2f6644;
    --field-light: #6f9a7c;
    --field-dark: #244f35;
    --gold: #e0b21a;
    --gold-rule: #a88a2a;
    --white: #ffffff;
  }
  * { margin: 0; padding: 0; box-sizing: border-box; }
  html, body {
    width: 1200px; height: 900px; overflow: hidden;
    background: var(--panel-green);
  }
  .slide {
    position: relative; width: 1200px; height: 900px; overflow: hidden;
    font-family: "Tinos", "Times New Roman", serif;
    color: var(--white);
  }
  .chart-backdrop {
    position: absolute; left: 745px; top: 0; width: 455px; height: 900px;
    background:
      radial-gradient(ellipse at 60% 20%, var(--field-light) 0%, transparent 45%),
      radial-gradient(ellipse at 70% 65%, #5c8a6b 0%, transparent 50%),
      linear-gradient(160deg, var(--field-green) 0%, #4b7d5c 45%, var(--field-dark) 100%);
  }
  .content-panel {
    position: absolute; left: 0; top: 0; width: 745px; height: 900px;
    background: var(--panel-green);
  }
  .slide-title {
    position: absolute; left: 33px; top: 46px;
    font-size: 34px; font-weight: 400; letter-spacing: 0.5px;
    color: var(--gold);
  }
  .title-rule {
    position: absolute; left: 0; top: 93px; width: 300px; height: 1.5px;
    background: var(--gold-rule);
  }
  .fund-heading {
    position: absolute; left: 36px; top: 150px;
    font-size: 22px; font-weight: 700; letter-spacing: 0.3px;
  }
  .benefit-list {
    position: absolute; left: 36px; top: 226px; width: 680px;
    list-style: none;
  }
  .benefit {
    position: relative; padding-left: 60px;
    font-size: 25px; line-height: 37.5px;
    margin-bottom: 23px;
  }
  .benefit svg {
    position: absolute; left: 6px; top: 9px; width: 22px; height: 20px;
  }
</style>
</head>
<body>
<div class="slide">
  <div class="chart-backdrop" role="img" aria-label="Photo of printed financial charts with bar graphs and a pie chart, tinted green"></div>
  <div class="content-panel">
    <h1 class="slide-title">WHY INVEST?</h1>
    <div class="title-rule"></div>
    <h2 class="fund-heading">CALLOWAY DERIVATIVES FUND, LP OFFERS:</h2>
    <ul class="benefit-list">
      <li class="benefit"><svg viewBox="0 0 22 20"><path d="M2 11 L8 17 L20 2" fill="none" stroke="#e0b21a" stroke-width="3.5" stroke-linecap="round" stroke-linejoin="round"/></svg>A large return potential</li>
      <li class="benefit"><svg viewBox="0 0 22 20"><path d="M2 11 L8 17 L20 2" fill="none" stroke="#e0b21a" stroke-width="3.5" stroke-linecap="round" stroke-linejoin="round"/></svg>Low risk over a 3 to 5 year horizon</li>
      <li class="benefit"><svg viewBox="0 0 22 20"><path d="M2 11 L8 17 L20 2" fill="none" stroke="#e0b21a" stroke-width="3.5" stroke-linecap="round" stroke-linejoin="round"/></svg>High liquidity (monthly withdrawals with no lockup period – subject to gate policy???)</li>
      <li class="benefit"><svg viewBox="0 0 22 20"><path d="M2 11 L8 17 L20 2" fill="none" stroke="#e0b21a" stroke-width="3.5" stroke-linecap="round" stroke-linejoin="round"/></svg>A Low minimum investment</li>
      <li class="benefit"><svg viewBox="0 0 22 20"><path d="M2 11 L8 17 L20 2" fill="none" stroke="#e0b21a" stroke-width="3.5" stroke-linecap="round" stroke-linejoin="round"/></svg>Transparent investment return properties</li>
      <li class="benefit"><svg viewBox="0 0 22 20"><path d="M2 11 L8 17 L20 2" fill="none" stroke="#e0b21a" stroke-width="3.5" stroke-linecap="round" stroke-linejoin="round"/></svg>Returns that do not correlate highly with returns in the stock and bond markets.&nbsp; The added diversification offered by the fund reduces an investor’s overall portfolio risk.</li>
      <li class="benefit"><svg viewBox="0 0 22 20"><path d="M2 11 L8 17 L20 2" fill="none" stroke="#e0b21a" stroke-width="3.5" stroke-linecap="round" stroke-linejoin="round"/></svg>Partnership in a small, agile fund that can generate returns that larger, less nimble, competitors cannot</li>
    </ul>
  </div>
</div>
</body>
</html>
```